Veldra Structural Approvals Private Assessors

Professional Construction Consultancy Company Business Card - must keep logo colours see images below - examples have been added from my last competition - please see them as examples only!

Target Market(s)

Home Builders

Industry/Entity Type

Construction

Contact Information for Business Card

See "must haves"

Font styles to use
Sans Serif

Colors
ffffff
add136
000000

Requirements
Must have
• Daniel Moravi
• Director
• Phone: 0431 587 219
• Address: 7 Tarrunga Rd,
• Hallworth Vale, SA, 5091
• Email: veldraassessors@mailbox-example.com
• Website: www.veldraassessors-example.com.au
• Facebook: Veldra Structural Approvals
Nice to have
• Side 1: full logo
• Side 2: company details
Should not have
• hard to read
• must be clear and professional

```html
<!DOCTYPE html>
<html lang="en">
<head>
<meta charset="utf-8">
<title>Veldra Structural Approvals – Business Card</title>
<link href="https://fonts.googleapis.com/css2?family=Montserrat:wght@400;600;700&family=Roboto:wght@400&display=swap" rel="stylesheet">
<style>
  :root {
    --green: #add136;
    --green-light: #c4e04a;
    --green-dark: #8fb52a;
    --white: #ffffff;
    --black: #000000;
    --ink: #333333;
    --rule: #d8d8d8;
    --stage: #ecebe6;
  }
  * { box-sizing: border-box; margin: 0; padding: 0; }
  html, body { width: 1200px; height: 1023px; overflow: hidden; background: var(--stage); }
  .canvas { position: relative; width: 1200px; height: 1023px; }

  .card {
    position: absolute; left: 180px; width: 840px; height: 480px;
    border-radius: 22px; overflow: hidden;
    box-shadow: 0 10px 30px rgba(0,0,0,.18);
  }
  .card--front { top: 22px; background: linear-gradient(135deg, #f4f4f4, var(--white) 50%, #f0f0f0); }
  .card--back { top: 522px; background: radial-gradient(ellipse at 60% 40%, var(--green-light), var(--green) 60%, var(--green-dark)); }

  /* front */
  .band { position: absolute; height: 16px; background: var(--green); }
  .band--top { top: 0; left: 0; width: 46%; }
  .band--bottom { bottom: 0; right: 0; width: 48%; }
  .divider { position: absolute; left: 50%; top: 40px; bottom: 40px; width: 1px; background: var(--rule); }

  .brand { position: absolute; left: 60px; top: 200px; width: 330px; display: flex; align-items: center; gap: 14px; }
  .brand__mark { flex: 0 0 34px; height: 34px; background: var(--green); }
  .brand__name { font-family: "Montserrat", sans-serif; font-weight: 700; font-size: 22px; line-height: 1.25; color: var(--black); text-transform: uppercase; letter-spacing: .5px; }

  .person { position: absolute; right: 48px; top: 40px; text-align: right; }
  .person__name { font-family: "Montserrat", sans-serif; font-weight: 400; font-size: 30px; color: var(--green); }
  .person__role { font-family: "Roboto", sans-serif; font-size: 17px; color: var(--black); margin-top: 2px; }
  .person__rule { position: absolute; right: 48px; top: 118px; width: 330px; height: 1px; background: var(--rule); }

  .skyline { position: absolute; left: 440px; top: 130px; width: 160px; height: 300px;
    background: linear-gradient(180deg, rgba(200,200,200,.06), rgba(190,190,190,.18)); }

  .contacts { position: absolute; right: 48px; top: 180px; list-style: none;
    font-family: "Roboto", sans-serif; font-size: 16px; color: var(--ink); text-align: right; }
  .contacts li { display: flex; justify-content: flex-end; align-items: center; gap: 10px; height: 36px; white-space: nowrap; }
  .icon { flex: 0 0 22px; width: 22px; height: 22px; border-radius: 4px; background: var(--green); display: flex; align-items: center; justify-content: center; }
  .icon svg { width: 14px; height: 14px; fill: none; stroke: var(--white); stroke-width: 2; }

  /* back */
  .back-brand { position: absolute; left: 0; right: 0; top: 160px; display: flex; flex-direction: column; align-items: center; gap: 18px; }
  .back-brand__row { display: flex; align-items: center; gap: 18px; }
  .back-brand__mark { width: 46px; height: 46px; background: var(--black); }
  .back-brand__name { font-family: "Montserrat", sans-serif; font-weight: 700; font-size: 34px; color: var(--black); text-transform: uppercase; letter-spacing: 1px; line-height: 1.2; }
  .back-brand__tag { font-family: "Montserrat", sans-serif; font-weight: 600; font-size: 22px; color: var(--white); letter-spacing: 12px; text-transform: uppercase; }
</style>
</head>
<body>
<div class="canvas">

  <section class="card card--front" aria-label="Business card, details side">
    <div class="band band--top"></div>
    <div class="band band--bottom"></div>
    <div class="divider"></div>

    <div class="brand">
      <span class="brand__mark"></span>
      <span class="brand__name">Veldra Structural Approvals Private Assessors</span>
    </div>

    <div class="skyline" role="img" aria-label="Faint line drawing of city buildings"></div>

    <div class="person">
      <div class="person__name">Daniel Moravi</div>
      <div class="person__role">Director</div>
    </div>
    <div class="person__rule"></div>

    <ul class="contacts">
      <li>0431 587 219 <span class="icon"><svg viewBox="0 0 14 14"><path d="M3 1.5l2 2.5-1.2 1.5a7 7 0 0 0 4.7 4.7L10 9l2.5 2-1 2A10 10 0 0 1 1 2.5z"/></svg></span></li>
      <li>veldraassessors@mailbox-example.com <span class="icon"><svg viewBox="0 0 14 14"><rect x="1.5" y="3" width="11" height="8"/><path d="M1.5 3l5.5 4.5L12.5 3"/></svg></span></li>
      <li>www.veldraassessors-example.com.au <span class="icon"><svg viewBox="0 0 14 14"><circle cx="7" cy="7" r="5.5"/><path d="M1.5 7h11M7 1.5c-2.5 3-2.5 8 0 11M7 1.5c2.5 3 2.5 8 0 11"/></svg></span></li>
      <li>7 Tarrunga Rd, Hallworth Vale, SA, 5091 <span class="icon"><svg viewBox="0 0 14 14"><path d="M7 13s-4-4.5-4-7.5a4 4 0 0 1 8 0C11 8.5 7 13 7 13z"/><circle cx="7" cy="5.5" r="1.4"/></svg></span></li>
      <li>Veldra Structural Approvals <span class="icon"><svg viewBox="0 0 14 14"><circle cx="7" cy="7" r="4"/></svg></span></li>
    </ul>
  </section>

  <section class="card card--back" aria-label="Business card, logo side">
    <div class="back-brand">
      <div class="back-brand__row">
        <span class="back-brand__mark"></span>
        <span class="back-brand__name">Veldra Structural<br>Approvals</span>
      </div>
      <div class="back-brand__tag">Private Assessors</div>
    </div>
  </section>

</div>
</body>
</html>
```